Scotch Whisky Label design

To create a unique Label for private bottling of rare single malt island whisky. Distilled in 1997 the whisky is 23 years and from the Island Of Arran. Design should encompass front label+ technical information (volume /drink waring /Alcohol % etc - all to be supplied) for the back lablel. Label should be CMYK only for digital printing. Label can include the island name but only as secondary information as thre brand Brackvane Malt Whisky is protected. Size of front label = approx 80mm x 120mm(portrait).

Design should be simple and effective, but to show quality and uniqueness of whisky

reference web link for ideas

https://www.peatcaskbidhall.example/auctions/148_the-52nd-sale/?page=12&area=

images show other similar items

images also show options for bottle style

Target Market(s)

Private buyers of rare whisky

Requirements
Must have
• Age of whisky (23 years)
• Single Island Brackvane Malt (in sub text)
Nice to have
• Traditonal illustration, reference of island geography
Should not have
• metalics,

```html
<!DOCTYPE html>
<html lang="en">
<head>
<meta charset="utf-8">
<title>Single Malt Island Whisky – Front Label</title>
<link href="https://fonts.googleapis.com/css2?family=Oswald:wght@300;400&family=Playfair+Display:wght@900&family=Libre+Baskerville&display=swap" rel="stylesheet">
<style>
  :root {
    --page: #f5f5f7;
    --label: #221f20;
    --gold: #b38b2f;
    --gold-soft: #a07a28;
    --brown: #6a4620;
    --cream: #f3efe6;
    --sepia-light: #d9d0bf;
    --sepia-dark: #8a6a3a;
  }
  * { margin: 0; padding: 0; box-sizing: border-box; }
  html, body { width: 1200px; height: 1200px; overflow: hidden; background: var(--page); }
  .front-label {
    position: absolute; left: 312px; top: 60px;
    width: 576px; height: 1080px;
    background: var(--label);
    color: var(--gold);
    font-family: "Libre Baskerville", serif;
  }
  .inner-frame { position: absolute; inset: 12px; border: 2px solid var(--gold-soft); }
  .rule-bar { position: absolute; }
  .rule-bar.top { top: 80px; }
  .rule-bar.bottom { top: 1010px; }
  .rule-bar.left { left: 36px; }
  .rule-bar.right { right: 36px; }
  .category {
    position: absolute; top: 140px; width: 100%; text-align: center;
    font-family: "Oswald", sans-serif; font-weight: 300;
    font-size: 50px; letter-spacing: 3px; line-height: 1;
  }
  .spirit {
    position: absolute; top: 210px; width: 100%; text-align: center;
    font-family: "Playfair Display", serif; font-weight: 900;
    font-size: 58px; letter-spacing: 2px; line-height: 1;
  }
  .vintage {
    position: absolute; top: 345px; width: 100%; text-align: center;
    font-size: 20px; letter-spacing: 6px; line-height: 1;
  }
  .age-line {
    position: absolute; top: 395px; left: 60px; right: 60px;
    display: flex; align-items: center; justify-content: center; gap: 22px;
    font-family: "Oswald", sans-serif; font-weight: 400;
  }
  .age-line .rule { flex: 1; height: 2px; background: var(--gold); }
  .age-line .word { font-size: 34px; letter-spacing: 4px; line-height: 1; }
  .age-line .number { font-size: 96px; line-height: 1; color: var(--cream); }
  .origin-note {
    position: absolute; top: 528px; width: 100%; text-align: center;
    font-size: 22px; color: var(--brown); letter-spacing: 0.5px;
  }
  .island-view {
    position: absolute; left: 108px; top: 598px; width: 360px; height: 244px;
    background: linear-gradient(180deg, var(--sepia-light) 0%, #cdbb98 40%, var(--sepia-dark) 58%, #cfc4b0 72%, var(--sepia-light) 100%);
  }
  .provenance {
    position: absolute; top: 888px; width: 100%; text-align: center;
    font-size: 14px; letter-spacing: 1px;
  }
  .volume, .strength {
    position: absolute; top: 955px;
    font-family: "Oswald", sans-serif; font-weight: 300; font-size: 38px; line-height: 1;
  }
  .volume { left: 84px; }
  .strength { right: 60px; }
  .strength small { font-size: 24px; }
</style>
</head>
<body>
  <main class="front-label">
    <div class="inner-frame"></div>

    <svg class="rule-bar top left" width="206" height="20" viewBox="0 0 206 20" aria-hidden="true">
      <rect x="0" y="14" width="206" height="2" fill="var(--gold)"/>
      <rect x="20" y="4" width="176" height="8" fill="none" stroke="var(--gold)" stroke-width="2"/>
    </svg>
    <svg class="rule-bar top right" width="206" height="20" viewBox="0 0 206 20" aria-hidden="true">
      <rect x="0" y="14" width="206" height="2" fill="var(--gold)"/>
      <rect x="10" y="4" width="176" height="8" fill="none" stroke="var(--gold)" stroke-width="2"/>
    </svg>

    <h1 class="category">SINGLE MALT ISLAND</h1>
    <h2 class="spirit">WHISKY</h2>

    <p class="vintage">DISTILLED 1997</p>
    <div class="age-line">
      <span class="rule"></span>
      <span class="word">AGED</span>
      <span class="number">23</span>
      <span class="word">YEARS</span>
      <span class="rule"></span>
    </div>

    <p class="origin-note">SINGLE ISLAND BRACKVANE MALT</p>

    <div class="island-view" role="img" aria-label="Sepia illustration of island mountains across calm water with a small sailing boat"></div>

    <p class="provenance">DISTILLED AND BOTTLED IN SCOTLAND</p>

    <p class="volume">70cl</p>
    <p class="strength">45<small>%</small> abv</p>

    <svg class="rule-bar bottom left" width="220" height="20" viewBox="0 0 220 20" aria-hidden="true">
      <rect x="0" y="4" width="220" height="2" fill="var(--gold)"/>
      <rect x="14" y="8" width="196" height="8" fill="none" stroke="var(--gold)" stroke-width="2"/>
    </svg>
    <svg class="rule-bar bottom right" width="220" height="20" viewBox="0 0 220 20" aria-hidden="true">
      <rect x="0" y="4" width="220" height="2" fill="var(--gold)"/>
      <rect x="10" y="8" width="196" height="8" fill="none" stroke="var(--gold)" stroke-width="2"/>
    </svg>
  </main>
</body>
</html>
```